Web Site for Strategy and Technology Consulting Company

We are looking for a website design that engages potential customers to understand our services and contact us. In this contest, we are looking for a homepage design, but the winning designer will be favored for the design of some of the more complicated interior pages of the site. An additional contest (or contests) for these pages will be added soon.

PLATROM AND RESPONSIVE DESIGN
The site will be implemented in WordPress using the Elementor page builder.
We are looking for a design that will look good on phones are well as laptop browsers.

UPLOADED FILES INCLUDE:
1a A wireframe of the homepage we are looking for. The Uploaded PDF also includes a draft of the text proposed for the homepage. Designers are free to go beyond the wireframe, but all elements of the wireframe should be included.
1b A Word document with the draft text of the homepage.
2a-d The Norvalith logo. Two versions are included – a dark version which works well against a light background, and a light version which works well against a dark background.
3 The Norvalith color palette with HEX and RGB values. Designers are not limited to this palette, but colors should be complementary.
4 A draft of the homepage menu
5 Service sheets with information on the services we provide

MORE ABOUT NORVALITH
Norvalith is a consulting company focused on transforming businesses through software. Our tagline, “Transformation Delivered,” recognizes the gap business often have between business transformation and the software they end up with. By listening to our customers and understanding their vision and where they are, we help get our customers where they want to go.

We increase our capability by working with many consultants and partners, allowing us to provide our customers with the best people and the software that best suits them.

Industry/Entity Type

Consulting

Number of Pages Required

1 page

Font styles to use
Sans Serif

Requirements
Must have
• the content represented on the wireframe uploaded
Nice to have
• interactive features, such as roll-over icons that reveal additional information

```html
<!DOCTYPE html>
<html lang="en">
<head>
<meta charset="utf-8">
<title>Norvalith – Homepage Hero Concepts</title>
<link rel="stylesheet" href="https://fonts.googleapis.com/css2?family=Noto+Sans:wght@400;600;700&display=swap">
<style>
  :root {
    --stage-bg: #b9d1e1;
    --white: #ffffff;
    --ink: #111111;
    --accent: #e3b511;
    --logo-grey: #d9dde2;
    --space-top: #000000;
    --space-horizon: #1d4f7e;
    --space-earth: #8fb1cf;
    --road-dark: #5a4430;
    --road-mid: #8c6c4c;
    --road-light: #b79674;
    --sea-light: #5aa0cc;
    --sea-mid: #1d6fa6;
    --sea-deep: #0b3f74;
    --reef: #2c4a4a;
  }
  * { box-sizing: border-box; margin: 0; padding: 0; }
  html, body { width: 1200px; height: 859px; overflow: hidden; }
  body {
    background: var(--stage-bg);
    font-family: "Noto Sans", sans-serif;
    position: relative;
  }
  .screen {
    position: absolute;
    width: 638px;
    height: 255px;
    overflow: hidden;
    color: var(--white);
    box-shadow: 0 4px 14px rgba(20, 40, 60, 0.28);
  }
  .screen--space { left: 75px; top: 77px; }
  .screen--road  { left: 281px; top: 302px; }
  .screen--ocean { left: 487px; top: 527px; }

  .hero-backdrop { position: absolute; inset: 0; }
  .screen--space .hero-backdrop {
    background: linear-gradient(180deg, var(--space-top) 0%, var(--space-top) 78%, var(--space-horizon) 86%, var(--space-earth) 100%);
  }
  .screen--road .hero-backdrop {
    background:
      linear-gradient(90deg, transparent 40%, rgba(70,70,70,0.55) 46%, rgba(90,90,90,0.55) 54%, transparent 60%),
      linear-gradient(180deg, var(--road-mid) 0%, var(--road-light) 35%, var(--road-mid) 65%, var(--road-dark) 100%);
  }
  .screen--ocean .hero-backdrop {
    background:
      linear-gradient(90deg, transparent 55%, rgba(44,74,74,0.55) 75%, var(--reef) 100%),
      linear-gradient(180deg, var(--sea-light) 0%, var(--sea-mid) 55%, var(--sea-deep) 100%);
  }
  .hero-figure { position: absolute; border-radius: 40%; }
  .screen--space .hero-figure { left: 285px; top: 10px; width: 58px; height: 64px; background: radial-gradient(ellipse, #e6e6e6 0%, #9a9a9a 55%, transparent 72%); }
  .screen--ocean .hero-figure { left: 180px; top: 45px; width: 50px; height: 130px; background: radial-gradient(ellipse, rgba(40,60,80,0.7) 0%, transparent 70%); }

  .site-logo {
    position: absolute;
    left: 17px;
    top: 8px;
    font-size: 17px;
    font-weight: 400;
    color: var(--logo-grey);
    letter-spacing: 0.2px;
  }

  .main-nav {
    position: absolute;
    top: 11px;
    left: 0;
    width: 100%;
    height: 14px;
  }
  .main-nav .nav-link {
    position: absolute;
    top: 0;
    height: 14px;
    line-height: 14px;
    font-size: 5.4px;
    font-weight: 600;
    color: var(--white);
    text-decoration: none;
    white-space: nowrap;
  }
  .main-nav .nav-home     { left: 395px; }
  .main-nav .nav-about    { left: 425px; }
  .main-nav .nav-services { left: 465px; }
  .main-nav .nav-insights { left: 502px; }
  .main-nav .nav-join     { left: 538px; }
  .main-nav .nav-link.is-active::after {
    content: "";
    position: absolute;
    left: 0; right: 0; bottom: 1px;
    height: 1px;
    background: var(--accent);
  }
  .main-nav .nav-contact {
    left: 573px;
    width: 48px;
    border-radius: 7px;
    background: var(--white);
    color: var(--ink);
    text-align: center;
  }

  .hero-title, .hero-lead, .hero-body {
    position: absolute;
    left: 0; right: 0;
    text-align: center;
    white-space: nowrap;
  }
  .hero-title { font-size: 18.6px; font-weight: 700; line-height: 1; top: 77px; }
  .hero-lead { font-size: 10.6px; font-weight: 600; top: 103px; }
  .hero-body { font-size: 9.3px; line-height: 12.7px; top: 129px; }
  .hero-cta {
    position: absolute;
    top: 166px;
    left: 288px;
    width: 63px; height: 16px;
    border-radius: 8px;
    background: var(--accent);
    color: var(--white);
    font-size: 8.2px;
    font-weight: 600;
    line-height: 16px;
    text-align: center;
    text-decoration: none;
  }
  .screen--ocean .hero-title { top: 88px; }
  .screen--ocean .hero-lead { top: 114px; }
  .screen--ocean .hero-body { top: 140px; }
  .screen--ocean .hero-cta { top: 178px; }

  .slide-dots { position: absolute; top: 238px; left: 302px; display: flex; gap: 8px; }
  .slide-dots span { width: 5px; height: 5px; border-radius: 50%; border: 0.8px solid var(--white); }
  .slide-dots span.is-current { background: var(--white); }

  .scroll-cue {
    position: absolute;
    top: 236px;
    left: 571px;
    display: flex;
    align-items: center;
    gap: 5px;
    font-size: 5.2px;
    font-weight: 600;
  }
</style>
</head>
<body>

  <section class="screen screen--space">
    <div class="hero-backdrop" role="img" aria-label="Astronaut floating in black space above the curve of the Earth"></div>
    <div class="hero-figure" role="img" aria-label="Astronaut in a white spacesuit"></div>
    <div class="site-logo">Norvalith</div>
    <nav class="main-nav">
      <a class="nav-link nav-home is-active" href="#">Home</a>
      <a class="nav-link nav-about" href="#">About Us</a>
      <a class="nav-link nav-services" href="#">Services</a>
      <a class="nav-link nav-insights" href="#">Insights</a>
      <a class="nav-link nav-join" href="#">Join Us</a>
      <a class="nav-link nav-contact" href="#">Contact Us</a>
    </nav>
    <h1 class="hero-title">Transformation Delivered</h1>
    <p class="hero-lead">We do more for our customers than implement software. WE LISTEN!</p>
    <p class="hero-body">We work to understand where they are in their<br>transformation journey and where they want to go.</p>
    <a class="hero-cta" href="#">Learn more</a>
  </section>

  <section class="screen screen--road">
    <div class="hero-backdrop" role="img" aria-label="Two travellers looking down a long straight road through brown rocky moorland"></div>
    <div class="site-logo">Norvalith</div>
    <nav class="main-nav">
      <a class="nav-link nav-home is-active" href="#">Home</a>
      <a class="nav-link nav-about" href="#">About Us</a>
      <a class="nav-link nav-services" href="#">Services</a>
      <a class="nav-link nav-insights" href="#">Insights</a>
      <a class="nav-link nav-join" href="#">Join Us</a>
      <a class="nav-link nav-contact" href="#">Contact Us</a>
    </nav>
    <h1 class="hero-title">Transformation Delivered</h1>
    <p class="hero-lead">We do more for our customers than implement software. WE LISTEN!</p>
    <p class="hero-body">We partner with them to clear the<br>roadblocks that stand in their way</p>
    <a class="hero-cta" href="#">Learn more</a>
  </section>

  <section class="screen screen--ocean">
    <div class="hero-backdrop" role="img" aria-label="Free diver swimming down through blue water beside a coral reef"></div>
    <div class="hero-figure" role="img" aria-label="Diver with long fins"></div>
    <div class="site-logo">Norvalith</div>
    <nav class="main-nav">
      <a class="nav-link nav-home is-active" href="#">Home</a>
      <a class="nav-link nav-about" href="#">About Us</a>
      <a class="nav-link nav-services" href="#">Services</a>
      <a class="nav-link nav-insights" href="#">Insights</a>
      <a class="nav-link nav-join" href="#">Join Us</a>
      <a class="nav-link nav-contact" href="#">Contact Us</a>
    </nav>
    <h1 class="hero-title">Transformation Delivered</h1>
    <p class="hero-lead">We do more for our customers than implement software. WE LISTEN!</p>
    <p class="hero-body">We ensure they reach their destination.</p>
    <a class="hero-cta" href="#">Learn more</a>
    <div class="slide-dots"><span class="is-current"></span><span></span><span></span></div>
    <div class="scroll-cue">
      <span>Scroll Down</span>
      <svg width="9" height="9" viewBox="0 0 10 10" aria-hidden="true">
        <circle cx="5" cy="5" r="4.3" fill="none" stroke="#ffffff" stroke-width="0.8"/>
        <path d="M5 2.6 V7 M3.2 5.3 L5 7.1 L6.8 5.3" fill="none" stroke="#ffffff" stroke-width="0.8"/>
      </svg>
    </div>
  </section>

</body>
</html>
```